Certificate of Completion - Educational Trainings

We are looking for a certificate of completion for individuals who complete one of our specific trainings. Files should be provided in a Word (docx) or PowerPoint (pptx) format. The "Halvorcrest example.png" file is to show necessary information. Copies of logos have been included for design purposes.

Target Market(s)

Training Participants

Industry/Entity Type

Healthcare

Font styles to use
Sans Serif

```html
<!DOCTYPE html>
<html lang="en">
<head>
<meta charset="utf-8">
<title>Halvorcrest Certificate of Completion</title>
<link href="https://fonts.googleapis.com/css2?family=Montserrat:wght@800&family=Poppins:wght@300;400;500&family=Great+Vibes&family=Allura&display=swap" rel="stylesheet">
<style>
  :root {
    --green-light: #6ab04c;
    --green-dark: #176b38;
    --green-line: #4fa34a;
    --ink: #111111;
    --paper: #ffffff;
  }
  * { margin: 0; padding: 0; box-sizing: border-box; }
  html, body { width: 788px; height: 1200px; overflow: hidden; background: var(--paper); }
  .certificate {
    position: relative; width: 788px; height: 1200px; background: var(--paper);
    font-family: "Poppins", sans-serif; color: var(--ink); text-align: center;
  }
  .certificate p, .certificate h1, .certificate h2 { line-height: 1.2; }
  .border-band { position: absolute; left: 0; width: 788px; height: 56px; background: linear-gradient(180deg, var(--green-light), #5a9f42); }
  .border-band--top { top: 0; }
  .border-band--bottom { bottom: 0; }
  .frame-side { position: absolute; top: 198px; bottom: 158px; width: 1.5px; background: var(--green-line); }
  .frame-side--left { left: 19px; }
  .frame-side--right { right: 19px; }
  .content { position: absolute; inset: 0; }
  .brand-dot { position: absolute; left: 366px; top: 118px; width: 56px; height: 56px; border-radius: 50%; background: var(--green-dark); }
  .brand-name { position: absolute; top: 212px; width: 100%; font-family: "Montserrat", sans-serif; font-weight: 800; font-size: 31px; letter-spacing: 1.5px; }
  .brand-address { position: absolute; top: 280px; width: 100%; font-size: 10.5px; font-weight: 400; letter-spacing: 0.3px; }
  .registry { position: absolute; top: 338px; width: 100%; font-size: 12px; font-weight: 300; }
  .title { position: absolute; top: 388px; width: 100%; font-size: 60px; font-weight: 500; letter-spacing: 3px; color: var(--green-dark); }
  .subtitle { position: absolute; top: 514px; width: 100%; font-family: "Great Vibes", cursive; font-size: 31px; }
  .awarded { position: absolute; top: 588px; width: 100%; font-size: 13px; font-weight: 300; letter-spacing: 0.4px; }
  .recipient { position: absolute; top: 648px; width: 100%; font-family: "Allura", cursive; font-size: 38px; color: var(--green-light); }
  .recipient-line { position: absolute; top: 718px; left: 237px; width: 314px; height: 1.5px; background: var(--green-dark); }
  .course { position: absolute; top: 756px; width: 100%; font-size: 14px; font-weight: 300; }
  .course span { display: block; line-height: 34px; }
  .sign { position: absolute; top: 951px; width: 158px; border-top: 1.5px solid var(--green-line); }
  .sign span { display: block; padding-top: 28px; font-size: 13px; font-weight: 300; letter-spacing: 0.3px; }
  .sign--date { left: 138px; }
  .sign--consultant { right: 138px; }
  .footnote { position: absolute; top: 1064px; width: 100%; font-size: 10px; font-weight: 300; }
  .footnote span { display: block; line-height: 16px; }
</style>
</head>
<body>
<main class="certificate">
  <div class="border-band border-band--top" role="img" aria-label="Decorative green border band"></div>
  <div class="border-band border-band--bottom" role="img" aria-label="Decorative green border band"></div>
  <div class="frame-side frame-side--left"></div>
  <div class="frame-side frame-side--right"></div>

  <section class="content">
    <div class="brand-dot"></div>
    <h1 class="brand-name">HALVORCREST</h1>
    <p class="brand-address">48 HARBOR LANE, STE. 310, WESTBROOK, ME 04092</p>
    <p class="registry">National registry sponsor number 71358</p>
    <h2 class="title">CERTIFICATE</h2>
    <p class="subtitle">of Completion</p>
    <p class="awarded">THIS CERTIFICATE IS AWARDED TO</p>
    <p class="recipient">Marisol Dunleavy</p>
    <div class="recipient-line"></div>
    <p class="course">
      <span>For Successful Completion of</span>
      <span>Best Practices: Budget Process/Budget Building</span>
      <span>Completed online Field of Study</span>
      <span>Finance CPE Credits: 1</span>
    </p>
    <div class="sign sign--date"><span>COMPLETION DATE</span></div>
    <div class="sign sign--consultant"><span>SENIOR CONSULTANT</span></div>
    <p class="footnote">
      <span>In accordance with the standard of the national registry of CPE Sponsors.</span>
      <span>CPE credits have been granted based on a 50 minute hour.</span>
    </p>
  </section>
</main>
</body>
</html>
```